Poster-style graphics needed for "rock star" Storytelling Coach

Thanks for your interest in my project. I need the FRONT COVER and BACK COVER for our 2018-9 Strategic Storytelling Programs brochure.

I run skills development events for Zenith 700s like Vorel Trust, Kavro, HoltzerWagen, Quarn, Pixwell, etc. The idea is to have first impression of "wow" design and impact that this is SOMETHING DIFFERENT from the usual corporate blah blah blah stuff.

Your inspiration will be from exciting movie posters featuring 5-star reviews ... ( I include a few examples as reference)

This brief is only for Front and Back Cover. (Don't worry about inside - we will use existing program brochure outlines for this). Have fun!

Output: A4 Portrait (VERTICAL) format, colour, PDF and jpeg.

Oh, the really good news is this: whoever wins this, will also get to work on the cover designs for my other company's programs too.

Target Market(s)

Zenith 700 corporates in Asia Pacific - might be HR or CEO or Marketing Department reading it. But it must be "exciting" not "corporate boring square and grey"

Industry/Entity Type

Training

Font styles to use
Sans Serif

Colors
fbed22
f78f20
ec1f27
33a6d7

Requirements
Must have
• FRONT COVER:
• 1.Ned Farrow pic on front cover - front and centre.
• 2. Must look like a 'movie poster' with 5 star reviews, Make it appear important, credible, exciting - make them want to read and share the brochure.
• 3. Reviews (as supplied below) big and bold on the front.
• 4. Headline: Hi, I'm Ned Farrow. "The Perfect Storyteller!" - The Morning Ledger, UK.
• Subhead: Strategic Storytelling & Presentation Literacy Skills Events 2018-9.
• 4. OWLBOXPIG logo. www.owlboxpig-example.com
• --
• BACK COVER:
• 1. Maybe a montage of shots (as provided) to show workshops and activities.
• 2. OWLBOXPIG logo
• 3. Call to action:
• Imagine what we could do for you! To unleash your team's strategic storytelling power, contact OWLBOXPIG today:
• bigpig@owlboxpig-example.com
• Asia/Pacific Storyline +66-91-305-7142.
• Heart Office: 5F Pak Tai Building, 42 Wexmore Street, Sheung Wan, Hong Kong.
• www.owlboxpig-example.com
• See more stories and clips at youtube: fablemaker47
• facebook.com/OWLBOXPIG
• --
• Reviews for front page: (use as many as you can/like ... the last ones are the least important ones)
• “You rock! The tips you shared will help me immensely in creating more potent and engaging content.” Producer/Anchor, Lumen Berita TV, Malaysia.
• “Great! Best course I have taken so far. Ned is an expert in his field. 10/10!” Dr KPN, Director, Medrova, China.
• “You have transformed the team in a day!” Director O&D, Asia Pacific, Brightwell Vanta.
• “Fantastic! Inspiring, fun, practical – That’s his magic dust. Some of the best training in my 25-year career. ” Managing Director, QUERIX.
• “Very inspiring and engaging teacher with highly positive energy. I learned a lot!” Regional Marketing Manager, Chirpdeck, Singapore.
• “Wonderful. Your energy and professional coaching are so impressive. The skills you taught are very helpful.” Lead R&D Engineer, TM, China.
• “Yeah! Yeah! Yeah! You’re the man, Ned. You helped me a lot in making my talk tighter … really appreciated!” Paul Wenrick, Frozen Harbor Haul (Corvin Prize-winning program airing in 200 countries), Horizon Network.
• “Thank you, Ned, for being such an amazing coach. The best of the best – I actually look forward to presentations now. !” Regional Financial Manager, APMEA, Wayfen Tours.
• "Ned is truly a subject matter expert." Marketing Executive, Vorel Trust, Singapore.

```html
<!DOCTYPE html>
<html lang="en">
<head>
<meta charset="utf-8">
<title>OWLBOXPIG – Strategic Storytelling Events 2018-9</title>
<link rel="stylesheet" href="https://fonts.googleapis.com/css2?family=Barlow+Condensed:ital,wght@0,400;0,800;1,600;1,700&family=Barlow:wght@400&display=swap">
<style>
  :root {
    --page-bg: #e9e9e9;
    --star-yellow: #fbed22;
    --brand-orange: #f78f20;
    --brand-red: #ec1f27;
    --brand-blue: #33a6d7;
    --ink-light: #f2efe8;
    --ink-muted: #d6d0c4;
    --smoke-warm: #b9a47a;
    --smoke-mid: #5a4c35;
    --night: #0d0d12;
  }
  * { box-sizing: border-box; margin: 0; padding: 0; }
  html, body { width: 1200px; height: 1200px; overflow: hidden; }
  body { background: var(--page-bg); position: relative; }

  .poster {
    position: absolute; left: 175px; top: 0;
    width: 850px; height: 1200px; overflow: hidden;
    background:
      radial-gradient(ellipse 380px 420px at 760px 300px, rgba(238,226,190,.75), transparent 70%),
      radial-gradient(ellipse 520px 460px at 380px 420px, rgba(150,128,88,.75), transparent 75%),
      radial-gradient(ellipse 600px 300px at 420px 900px, rgba(120,108,90,.55), transparent 75%),
      linear-gradient(180deg, var(--smoke-mid) 0%, #2b261d 45%, #17161a 75%, var(--night) 100%);
    color: var(--ink-light);
  }

  .hero-photo {
    position: absolute; left: 285px; top: 145px; width: 360px; height: 640px;
    border-radius: 46% 46% 30% 30%;
    background: radial-gradient(ellipse at 50% 30%, #c98d62 0%, #7a4f36 28%, #2a211c 60%, rgba(20,18,18,0) 78%);
  }

  .review { position: absolute; width: 270px; text-align: center; transform: translateX(-50%); }
  .review .stars { display: block; margin: 0 auto 14px; }
  .review .quote {
    font-family: "Barlow Condensed", sans-serif; font-style: italic; font-weight: 600;
    font-size: 15px; line-height: 20px; text-transform: uppercase; color: var(--star-yellow);
  }
  .review .source {
    margin-top: 12px;
    font-family: "Barlow Condensed", sans-serif; font-weight: 400;
    font-size: 10.5px; line-height: 14px; text-transform: uppercase; color: var(--ink-muted);
  }

  .greeting {
    position: absolute; left: 140px; top: 738px;
    font-family: "Barlow Condensed", sans-serif; font-style: italic; font-weight: 700;
    font-size: 54px; letter-spacing: -1px; color: var(--ink-light);
    text-transform: uppercase;
  }
  .brand-name {
    position: absolute; left: 95px; width: 660px; top: 812px; text-align: center;
    font-family: "Barlow Condensed", sans-serif; font-weight: 800;
    font-size: 108px; line-height: 1; letter-spacing: 10px; color: var(--ink-light);
  }
  .tagline {
    position: absolute; left: 0; width: 850px; top: 935px; text-align: center;
    font-family: "Barlow Condensed", sans-serif; font-style: italic; font-weight: 600;
    font-size: 54px; line-height: 60px; color: var(--ink-light);
  }
  .credit {
    position: absolute; right: 100px; top: 1004px;
    font-family: "Barlow Condensed", sans-serif; font-style: italic; font-weight: 600;
    font-size: 34px; color: var(--ink-light);
  }
  .subhead {
    position: absolute; left: 0; width: 850px; top: 1090px; text-align: center;
    font-family: "Barlow", sans-serif; font-size: 19px; letter-spacing: 1.4px; color: var(--ink-muted);
  }
</style>
</head>
<body>
<svg width="0" height="0" style="position:absolute">
  <defs>
    <symbol id="star" viewBox="0 0 24 24">
      <path d="M12 1.5l3.1 7 7.6.7-5.8 5 1.8 7.5L12 17.8 5.3 21.7l1.8-7.5-5.8-5 7.6-.7z" fill="#fbed22"/>
    </symbol>
    <symbol id="five-stars" viewBox="0 0 160 30">
      <use href="#star" x="0" y="0" width="30" height="30"/>
      <use href="#star" x="32.5" y="0" width="30" height="30"/>
      <use href="#star" x="65" y="0" width="30" height="30"/>
      <use href="#star" x="97.5" y="0" width="30" height="30"/>
      <use href="#star" x="130" y="0" width="30" height="30"/>
    </symbol>
  </defs>
</svg>

<main class="poster">
  <div class="hero-photo" role="img" aria-label="Portrait of coach Ned Farrow smiling, set against a smoky city skyline"></div>

  <section class="review" style="left:425px; top:32px;">
    <svg class="stars" width="160" height="30"><use href="#five-stars"/></svg>
    <p class="quote">“You have transformed the team in a day!”</p>
    <p class="source">Director O&amp;D, Asia Pacific,<br>Brightwell Vanta</p>
  </section>

  <section class="review" style="left:160px; top:97px;">
    <svg class="stars" width="160" height="30"><use href="#five-stars"/></svg>
    <p class="quote">“You rock! The tips you shared will help me immensely in creating more potent and engaging content.”</p>
    <p class="source">Producer/Anchor,<br>Lumen Berita TV, Malaysia.</p>
  </section>

  <section class="review" style="left:690px; top:97px;">
    <svg class="stars" width="160" height="30"><use href="#five-stars"/></svg>
    <p class="quote">“Very inspiring and engaging teacher with highly positive energy. I learned a lot!”</p>
    <p class="source">Regional Marketing Manager,<br>Chirpdeck, Singapore.</p>
  </section>

  <section class="review" style="left:160px; top:283px;">
    <svg class="stars" width="160" height="30"><use href="#five-stars"/></svg>
    <p class="quote">“Great! Best course I have taken so far. Ned is an expert in his field. 10/10!”</p>
    <p class="source">Dr KPN, Director, Medrova, China.</p>
  </section>

  <section class="review" style="left:690px; top:283px;">
    <svg class="stars" width="160" height="30"><use href="#five-stars"/></svg>
    <p class="quote">“Fantastic! Inspiring, fun, practical – that’s his magic dust. Some of the best training in my 25-year career.”</p>
    <p class="source">Managing Director, QUERIX</p>
  </section>

  <section class="review" style="left:160px; top:482px;">
    <svg class="stars" width="160" height="30"><use href="#five-stars"/></svg>
    <p class="quote">“Wonderful. Your energy and professional coaching are so impressive. The skills you taught are very helpful.”</p>
    <p class="source">Lead R&amp;D Engineer, TM, China.</p>
  </section>

  <section class="review" style="left:690px; top:482px;">
    <svg class="stars" width="160" height="30"><use href="#five-stars"/></svg>
    <p class="quote">“Yeah! Yeah! Yeah! You’re the man, Ned. You helped me a lot in making my talk tighter … really appreciated!”</p>
    <p class="source">Paul Wenrick, Frozen Harbor Haul<br>Horizon Network</p>
  </section>

  <h1 class="greeting">Hi, I’m Ned Farrow.</h1>

  <p class="brand-name">OWLBOXPIG</p>

  <p class="tagline">"The Perfect Storyteller!"</p>
  <p class="credit">- The Morning Ledger, UK.</p>

  <p class="subhead">Strategic Storytelling &amp; Presentation Literacy Skills Events 2018-9</p>
</main>
</body>
</html>
```